Makeup artist looking for business card design

- Business card to be memorable and recognisable

- I've attached photos of my logo (File 4), photos that I want to incorporate into the design (File 5,6 & 7) and an example of the design I like "Mirela Stott" (File 1)

- I've attached 3 photos of the designs I want to use, please use one of your choice

- Next to Instagram (File 2) and Facebook (File 3), please use their logo.

- No coloured background, either use the original background (grey) old white.

- Please include the following on the business card:
- Business name: LK Makeup Artistry
- My name: Rosalind Kerr
- Occupation: Makeup Artist
- Contact number: 0437 295 148
- Email: roskerr_makeup@mailvento.com
- Instagram (please use image): @lkmakeupartistry
- Facebook (please use image): www.pagenook.net/LKMakeUpArtistry

Target Market(s)

Target woman for bridal makeup, occasion, fashion makeup and print.

Industry/Entity Type

Business

Requirements
Must have
• Logo provided and photo provided
Should not have
• Colourful background
Too cluttered
Shouldn't use old style font

```html
<!DOCTYPE html>
<html lang="en">
<head>
<meta charset="utf-8">
<title>LK Makeup Artistry — Business Card</title>
<link href="https://fonts.googleapis.com/css2?family=Montserrat:wght@300;400&family=Open+Sans:wght@400&display=swap" rel="stylesheet">
<style>
  :root {
    --stage: #2b2b2d;
    --card: #ffffff;
    --panel: rgba(255, 255, 255, 0.9);
    --plum: #8b3a8f;
    --plum-soft: #b57ab5;
    --lilac: #d9a9d6;
    --lilac-pale: #f1e1ef;
    --ink: #3a3a3c;
    --ink-soft: #6b6b70;
    --skin: #e9c2b4;
  }
  * { box-sizing: border-box; margin: 0; padding: 0; }
  html, body {
    width: 1200px; height: 900px; overflow: hidden;
    background: var(--stage);
  }
  .canvas { position: relative; width: 1200px; height: 900px; }

  .card {
    position: absolute; left: 260px; width: 680px; height: 416px;
    background: var(--card); overflow: hidden;
    box-shadow: 0 10px 28px rgba(0,0,0,.45);
  }
  .card--contact { top: 22px; }
  .card--brand { top: 462px; }

  .photo-portrait {
    position: absolute; top: 0; left: 0; height: 100%;
    background: linear-gradient(135deg, #c99aa0 0%, var(--skin) 35%, #e7b3cf 60%, #b67bb4 100%);
  }
  .photo-blooms {
    position: absolute; top: 0; height: 100%;
    background: radial-gradient(circle at 40% 35%, #ffffff 0%, var(--lilac-pale) 30%, var(--lilac) 70%, #b77fb6 100%);
  }

  .card--contact .photo-blooms { left: 150px; width: 170px; }
  .card--contact .photo-portrait { width: 250px; }
  .card--contact .info-side {
    position: absolute; left: 300px; top: 0; width: 380px; height: 100%;
    background: var(--card);
  }

  .wordmark {
    display: flex; align-items: center; gap: 12px;
    font-family: "Montserrat", sans-serif; font-weight: 300;
    color: var(--ink); text-transform: uppercase; letter-spacing: 2px;
  }
  .wordmark__dot { width: 18px; height: 18px; border-radius: 50%; background: var(--ink); flex: none; }

  .card--contact .wordmark { position: absolute; left: 26px; top: 70px; width: 120px; font-size: 15px; line-height: 1.35; }

  .person { position: absolute; left: 160px; top: 72px; width: 205px; font-family: "Montserrat", sans-serif; }
  .person__name { font-size: 21px; font-weight: 400; color: var(--plum); text-transform: uppercase; letter-spacing: 0.5px; white-space: nowrap; }
  .person__role { font-size: 17px; font-weight: 300; color: var(--ink-soft); margin-top: 2px; }
  .person__rule { margin-top: 8px; width: 100%; height: 2px; background: linear-gradient(90deg, var(--plum-soft), var(--plum)); }

  .contacts {
    position: absolute; left: 40px; top: 230px; list-style: none;
    font-family: "Open Sans", sans-serif; font-size: 14px; color: var(--ink);
  }
  .contacts li { display: flex; align-items: center; gap: 12px; height: 32px; white-space: nowrap; }
  .contacts svg { width: 16px; height: 16px; fill: var(--plum); flex: none; }
  .contacts .mark { width: 14px; height: 14px; border-radius: 50%; background: var(--plum); flex: none; margin: 0 1px; }

  .card--brand .photo-blooms { left: 0; width: 100%; }
  .card--brand .photo-portrait { width: 330px; }
  .brand-panel {
    position: absolute; left: 352px; top: 0; width: 250px; height: 100%;
    background: var(--panel);
  }
  .card--brand .wordmark {
    position: absolute; left: 40px; top: 160px; width: 190px;
    font-size: 20px; line-height: 1.35;
  }
  .card--brand .wordmark__dot { width: 26px; height: 26px; }
  .social { position: absolute; right: 14px; bottom: 110px; display: flex; gap: 6px; }
  .social span { width: 22px; height: 22px; background: var(--ink-soft); border-radius: 3px; }
</style>
</head>
<body>
<main class="canvas">

  <section class="card card--contact" aria-label="Business card, contact side">
    <div class="photo-blooms" role="img" aria-label="Soft lilac flower petals"></div>
    <div class="photo-portrait" role="img" aria-label="Beauty portrait of a model wearing pink makeup"></div>
    <div class="info-side">
      <div class="wordmark"><span class="wordmark__dot"></span><span>LK Makeup Artistry</span></div>
      <div class="person">
        <p class="person__name">Rosalind Kerr</p>
        <p class="person__role">Makeup Artist</p>
        <div class="person__rule"></div>
      </div>
      <ul class="contacts">
        <li>
          <svg viewBox="0 0 24 24" aria-hidden="true"><path d="M6.6 10.8c1.4 2.8 3.8 5.1 6.6 6.6l2.2-2.2c.3-.3.7-.4 1-.2 1.1.4 2.3.6 3.6.6.6 0 1 .4 1 1V20c0 .6-.4 1-1 1C10.6 21 3 13.4 3 4c0-.6.4-1 1-1h3.5c.6 0 1 .4 1 1 0 1.3.2 2.5.6 3.6.1.3 0 .7-.2 1z"/></svg>
          <span>0437 295 148</span>
        </li>
        <li>
          <svg viewBox="0 0 24 24" aria-hidden="true"><path d="M3 5h18v14H3zM4.5 6.5v.4L12 12l7.5-5.1v-.4z"/></svg>
          <span>roskerr_makeup@mailvento.com</span>
        </li>
        <li><span class="mark"></span><span>@lkmakeupartistry</span></li>
        <li><span class="mark"></span><span>www.pagenook.net/LKMakeUpArtistry</span></li>
      </ul>
    </div>
  </section>

  <section class="card card--brand" aria-label="Business card, brand side">
    <div class="photo-blooms" role="img" aria-label="Large lilac flower petals"></div>
    <div class="photo-portrait" role="img" aria-label="Close-up beauty portrait of a model with purple eye makeup"></div>
    <div class="brand-panel">
      <div class="wordmark"><span class="wordmark__dot"></span><span>LK Makeup Artistry</span></div>
      <div class="social"><span></span><span></span></div>
    </div>
  </section>

</main>
</body>
</html>
```